Gelato Business Card

create a new business card using existing logo

Target Market(s)

B2B

Contact Information for Business Card

typical contact info: logo, address, email, phone, rep name

Colors
0355a3
33a6d7

Requirements
Must have
• a feel of high quality, luxury, happiness
• use cool, comforting color and texture of business card.
Nice to have
• "A Little Perfection Goes A Long Way!" TM
• or, "more quality, more flavor"
• or, "Flavor Matters"

```html
<!DOCTYPE html>
<html lang="en">
<head>
<meta charset="utf-8">
<title>Vellini's Business Card</title>
<link rel="stylesheet" href="https://fonts.googleapis.com/css2?family=Baloo+2:wght@500;600&display=swap">
<style>
  :root {
    --page: #ececea;
    --card: #f7f7f6;
    --sky: #4a9fd8;
    --violet: #3f3a96;
    --ink: #1c1c1c;
    --rule: #9a9a9a;
  }
  * { margin: 0; padding: 0; box-sizing: border-box; }
  html, body { width: 1200px; height: 1200px; overflow: hidden; }
  body {
    background: var(--page);
    display: flex;
    align-items: center;
    justify-content: center;
    font-family: "Baloo 2", sans-serif;
  }
  .business-card {
    position: relative;
    width: 1000px;
    height: 572px;
    background: var(--card);
    border-top: 10px solid var(--sky);
    border-bottom: 10px solid var(--violet);
    box-shadow: 0 10px 30px rgba(0,0,0,0.12);
    display: flex;
    align-items: center;
  }
  .brand {
    width: 560px;
    display: flex;
    align-items: center;
    justify-content: center;
    gap: 22px;
  }
  .brand-dot {
    width: 34px;
    height: 34px;
    border-radius: 50%;
    background: var(--violet);
  }
  .brand-name {
    font-size: 76px;
    font-weight: 600;
    color: var(--violet);
    letter-spacing: 1px;
  }
  .divider {
    width: 2px;
    height: 240px;
    background: var(--rule);
  }
  .contact {
    padding-left: 26px;
    font-weight: 500;
    line-height: 1.12;
    color: var(--ink);
  }
  .contact .address { font-size: 27px; }
  .contact .phone { font-size: 29px; color: var(--violet); font-weight: 600; }
  .contact .web { font-size: 22px; }
</style>
</head>
<body>
  <div class="business-card">
    <div class="brand">
      <span class="brand-dot"></span>
      <span class="brand-name">Vellini's</span>
    </div>
    <div class="divider"></div>
    <div class="contact">
      <p class="address">2450 Marlow Ave. Suite C,</p>
      <p class="address">Larkspur, CA 94939,</p>
      <p class="address">United States</p>
      <p class="phone">(415) 555-0142,</p>
      <p class="phone">(415) 555-0187 (fax)</p>
      <p class="web">www.vellinisgelato.com</p>
      <p class="web">questions@vellinisgelato.com</p>
    </div>
  </div>
</body>
</html>
```